Automotive Water Pump Inner Box Design

We are a wholesaler for Automotive Spare Parts in Jordan market and needs to import Water Pumps from Korea under our company private brand "TORVA".

Target Market(s)

JORDAN

Font styles to use
Serif

Colors
33a6d7
0692cd

Requirements
Must have
• WATER PUMP

MADE IN KOREA
Nice to have
• PHOTO OF WATER PUMP ON THE BOX

PANTONE COLOR is attached.

```html
<!DOCTYPE html>
<html lang="en">
<head>
<meta charset="UTF-8">
<title>TORVA Water Pump Inner Box</title>
<link rel="stylesheet" href="https://fonts.googleapis.com/css2?family=Barlow+Condensed:ital,wght@0,700;1,800&family=Open+Sans:wght@400&display=swap">
<style>
  :root {
    --bg: #ececec;
    --navy: #1b202c;
    --navy-deep: #161a24;
    --steel: #3f5f7c;
    --steel-light: #8fa4b6;
    --mist: #d6d8db;
    --title: #e4e4e4;
    --accent: #33a6d7;
    --accent-deep: #0692cd;
    --line-blue: #3f7cc6;
    --tagline: #8cc4ea;
    --metal: #9a9c9f;
  }
  * { margin: 0; padding: 0; box-sizing: border-box; }
  html, body { width: 1200px; height: 1200px; overflow: hidden; background: var(--bg); }
  .canvas { position: relative; width: 1200px; height: 1200px; }
  .panel { position: absolute; overflow: hidden; }
  .panel svg { display: block; }
  .panel-top { left: 430px; top: 170px; width: 640px; height: 300px; }
  .panel-side { left: 130px; top: 470px; width: 300px; height: 460px; }
  .panel-front { left: 430px; top: 470px; width: 640px; height: 460px; }
  .title { font-family: "Barlow Condensed", sans-serif; font-style: italic; font-weight: 800; fill: var(--title); }
  .brand { font-family: "Barlow Condensed", sans-serif; font-weight: 700; fill: var(--accent); letter-spacing: 2px; }
  .tagline { font-family: "Open Sans", sans-serif; font-weight: 400; fill: var(--tagline); }
  .origin { font-family: "Open Sans", sans-serif; font-weight: 400; fill: var(--title); letter-spacing: 1px; }
</style>
</head>
<body>
<div class="canvas">

  <div class="panel panel-top">
    <svg width="640" height="300" viewBox="0 0 640 300">
      <defs>
        <linearGradient id="topFade" x1="0" y1="0" x2="1" y2="0.3">
          <stop offset="0" stop-color="var(--navy)"/>
          <stop offset="0.5" stop-color="var(--navy)"/>
          <stop offset="0.78" stop-color="var(--steel)"/>
          <stop offset="1" stop-color="var(--mist)"/>
        </linearGradient>
      </defs>
      <rect class="lid-surface" width="640" height="300" fill="url(#topFade)"/>
      <g class="brand-mark">
        <circle cx="232" cy="72" r="14" fill="var(--accent)"/>
        <text class="brand" x="256" y="88" font-size="44">TORVA</text>
      </g>
      <text class="tagline" x="300" y="128" font-size="20" text-anchor="middle">Drives you further</text>
      <polyline class="title-rule" points="110,170 560,150 536,210" fill="none" stroke="var(--line-blue)" stroke-width="4"/>
      <text class="title" x="118" y="232" font-size="62">WATER PUMP</text>
    </svg>
  </div>

  <div class="panel panel-side">
    <svg width="300" height="460" viewBox="0 0 300 460">
      <defs>
        <linearGradient id="sideFade" x1="0" y1="0" x2="0" y2="1">
          <stop offset="0" stop-color="var(--navy)"/>
          <stop offset="0.55" stop-color="var(--navy)"/>
          <stop offset="1" stop-color="var(--steel)"/>
        </linearGradient>
      </defs>
      <rect class="side-surface" width="300" height="460" fill="url(#sideFade)"/>
      <g transform="translate(300,0) rotate(90)">
        <g class="brand-mark">
          <circle cx="40" cy="60" r="14" fill="var(--accent)"/>
          <text class="brand" x="64" y="76" font-size="44">TORVA</text>
        </g>
        <text class="tagline" x="56" y="112" font-size="20">Drives you further</text>
        <polyline class="title-rule" points="130,150 440,150 420,205" fill="none" stroke="var(--line-blue)" stroke-width="4"/>
        <text class="title" x="140" y="206" font-size="56">WATER PUMP</text>
        <text class="origin" x="220" y="262" font-size="20">MADE IN KOREA</text>
      </g>
    </svg>
  </div>

  <div class="panel panel-front">
    <svg width="640" height="460" viewBox="0 0 640 460">
      <defs>
        <linearGradient id="frontFade" x1="0" y1="0" x2="1" y2="0.15">
          <stop offset="0" stop-color="var(--navy-deep)"/>
          <stop offset="0.35" stop-color="var(--steel)"/>
          <stop offset="0.75" stop-color="var(--steel-light)"/>
          <stop offset="1" stop-color="var(--mist)"/>
        </linearGradient>
        <linearGradient id="pumpTone" x1="0" y1="0" x2="1" y2="1">
          <stop offset="0" stop-color="#b4b6b9"/>
          <stop offset="1" stop-color="var(--metal)"/>
        </linearGradient>
      </defs>
      <rect class="front-surface" width="640" height="460" fill="var(--navy)"/>
      <path class="front-band" d="M0,250 C200,240 420,215 640,190 L640,460 L0,460 Z" fill="url(#frontFade)"/>
      <polyline class="title-rule" points="20,78 600,52 525,160" fill="none" stroke="var(--line-blue)" stroke-width="4"/>
      <text class="title" x="40" y="162" font-size="92">WATER PUMP</text>
      <rect class="product-photo" x="345" y="170" width="275" height="270" rx="14" fill="url(#pumpTone)" role="img" aria-label="Photo of an automotive water pump"/>
      <g class="brand-mark">
        <circle cx="60" cy="362" r="15" fill="var(--accent)"/>
        <text class="brand" x="86" y="379" font-size="46">TORVA</text>
      </g>
      <text class="tagline" x="56" y="418" font-size="21">Drives you further</text>
    </svg>
  </div>

</div>
</body>
</html>
```